CREATE A KILLER WEBSITE DESIGN

We are a firearms training company that trains CIVILIANS (no police or military pictures - thank you!) to defend themselves and are looking for a killer design that's clean, easy to navigate and modern! We want the newest trends applied to this sight like a scrollable site so you can scroll down and see all the features. We are okay with tweaking the HTML but need the artistic design to look good. I'll provide a link to our current site along with a sight we really like so you can get an idea!

I'm supplying a PowerPoint Design we are going with from another designer so you can match the style to the new site.

PAGES: (Please use information from our current site. We like the information but just want a more polished look similar to the NWDFA site below but in our colors.)
Home - Long Form Scrolling Site. Top fold will be a video with a play button.
Falconry Institute - Seven Level Training Program Info Page That Will Contain A Video.
Contact Us - This will be a page that DOES NOT CONTAIN AN EMAIL ADDRESS. Just a contact us form
Meet The Trainer: Brendan Osterlow

Our site:
https://www.brightharborguarding.biz

Sights We Like:
https://www.nwdefenderalliance.com
https://quorvel.com
https://brinmoreworkscorp.com
https://www.pelldrivegear.com

Target Market(s)

Men and women ages 21 to 100 years old

Industry/Entity Type

Self Defense

Number of Pages Required

5+ page

Font styles to use
Sans Serif

Colors
f26267

Requirements
Must have
• Clean and engaging. Use of colors that match our logo.
Should not have
• Poor design quality

```html
<!DOCTYPE html>
<html lang="en">
<head>
<meta charset="utf-8">
<title>Bright Harbor Guarding</title>
<link href="https://fonts.googleapis.com/css2?family=Montserrat:wght@400;500;600;700;800;900&display=swap" rel="stylesheet">
<style>
:root{
  --red:#e4181b;
  --ink:#1a1a1a;
  --charcoal:#2b2b2b;
  --night:#1f1f1f;
  --paper:#f4f4f4;
  --white:#ffffff;
  --muted:#c9c9c9;
}
*{box-sizing:border-box;margin:0;padding:0}
html,body{width:1200px;height:3959px;overflow:hidden}
body{position:relative;font-family:'Montserrat',sans-serif;background:var(--paper);color:var(--ink)}
.abs{position:absolute}

/* header */
.site-nav{position:absolute;left:0;top:0;width:1200px;height:55px;background:var(--ink);z-index:3}
.site-nav a{position:absolute;top:19px;font-size:13px;font-weight:600;letter-spacing:1.6px;color:var(--white);text-decoration:none;text-transform:uppercase;white-space:nowrap}
.site-nav a.active,.site-nav a.login{color:var(--red)}
.brand{position:absolute;left:40px;top:16px;z-index:4;display:flex;align-items:center;gap:8px;color:var(--white);font-weight:800;font-size:15px;letter-spacing:1px}
.brand-dot{width:22px;height:22px;border-radius:50%;background:var(--red)}

/* hero */
.hero{position:absolute;left:0;top:55px;width:1200px;height:606px;background:linear-gradient(100deg,#1d3a39 0%,#3f6d6a 45%,#7c958e 75%,#b8c4b2 100%)}
.play-film{position:absolute;left:108px;top:332px;width:147px;height:43px;background:rgba(60,70,70,.85);color:var(--white);font-size:14px;font-weight:600;display:flex;align-items:center;justify-content:center;gap:9px}
.hero h1{position:absolute;left:103px;top:385px;font-size:60px;line-height:54px;font-weight:900;color:var(--white);letter-spacing:.5px;white-space:nowrap}
.btn{position:absolute;top:523px;height:44px;font-size:13px;font-weight:700;color:var(--white);display:flex;align-items:center;justify-content:center;text-transform:uppercase;white-space:nowrap}
.btn-solid{left:103px;width:237px;background:var(--red)}
.btn-ghost{left:364px;width:235px;border:2px solid var(--red)}

/* instructor */
.instructor{position:absolute;left:0;top:661px;width:1200px;height:622px;background:var(--charcoal)}
.eyebrow{font-size:14px;font-weight:600;letter-spacing:2.4px;color:var(--red);text-transform:uppercase}
.instructor h2{position:absolute;left:670px;top:144px;font-size:33px;font-weight:700;letter-spacing:3.5px;color:var(--white);white-space:nowrap}
.instructor p{position:absolute;left:670px;top:208px;width:440px;font-size:14px;line-height:31.2px;color:var(--white)}
.seen-on{position:absolute;left:0;top:504px;width:1200px;text-align:center}
.rule{height:3px;background:var(--red)}
.media-badge{position:absolute;top:1221px;width:122px;height:122px;border-radius:50%;background:var(--white);display:flex;align-items:center;justify-content:center;text-align:center;font-size:17px;font-weight:800;color:var(--ink);z-index:2}

/* training */
.training-title{position:absolute;left:103px;top:1428px;font-size:40px;line-height:54.5px;font-weight:800;letter-spacing:4.5px;text-transform:uppercase;white-space:nowrap}
.training-title .hl{color:var(--red)}
.training-copy{position:absolute;left:103px;top:1640px;width:360px;font-size:14px;line-height:31.2px;color:var(--ink)}
.level-card{position:absolute;top:1652px;height:258px;overflow:hidden}
.level-card .photo{position:absolute;inset:0 0 32px 0}
.level-card .label{position:absolute;left:0;right:0;bottom:0;height:32px;background:var(--red);color:var(--white);font-size:14px;font-weight:700;letter-spacing:1.8px;padding-left:24px;display:flex;align-items:center;white-space:nowrap}
.dots{position:absolute;left:738px;top:1956px;display:flex;gap:21.5px}
.dots span{width:12px;height:12px;border-radius:50%;background:var(--ink)}
.dots span.on{background:none;border:2px solid var(--ink)}

/* video */
.section-head{position:absolute;left:0;width:1200px;text-align:center;font-weight:700;text-transform:uppercase}
.video-band{position:absolute;left:0;top:2389px;width:1200px;height:914px;background:var(--night)}
.video-frame{position:absolute;left:195px;top:2159px;width:811px;height:461px;background:#3d3d3d;display:flex;align-items:center;justify-content:center}

/* stories */
.stories-photo{position:absolute;left:0;top:2620px;width:1200px;height:683px;background:radial-gradient(ellipse at 50% 45%,#4a4a4a 0%,#2b2b2b 45%,#1d1d1d 100%)}
.story{position:absolute;width:290px;color:var(--white)}
.story .quote{font-size:54px;font-weight:900;font-style:italic;color:var(--red);line-height:40px;height:50px}
.story p{font-size:17px;line-height:31.2px;margin-top:17px}
.story .who{margin-top:16px;font-size:16px;font-weight:700;color:var(--red);line-height:18px}
.story .when{font-size:13px;color:var(--white);line-height:16px}

/* contact */
.contact{position:absolute;left:0;top:3303px;width:1200px;height:587px;background:var(--red);color:var(--white)}
.contact h2{position:absolute;left:196px;top:144px;font-size:30px;font-weight:700;letter-spacing:2px;white-space:nowrap}
.contact .role{position:absolute;left:196px;top:202px;width:360px;font-size:13.5px;line-height:25px}
.contact .details{position:absolute;left:196px;top:312px;font-size:13.5px;line-height:16.5px;letter-spacing:.8px}
.contact .details div{margin-bottom:13px}
.field-label{position:absolute;left:628px;font-size:13px;color:var(--white)}
.field{position:absolute;left:628px;width:378px;border:2px solid var(--white)}
.send{position:absolute;left:628px;top:471px;width:378px;height:38px;background:var(--white);color:var(--ink);font-size:15px;font-weight:600;letter-spacing:4px;display:flex;align-items:center;justify-content:center}
.site-footer{position:absolute;left:0;top:3890px;width:1200px;height:69px;background:var(--charcoal);color:var(--white);font-size:13.5px;display:flex;align-items:center;justify-content:center}
</style>
</head>
<body>

<header class="site-nav">
  <a class="active" style="left:364px">Home</a>
  <a style="left:449px">Falconry Institute</a>
  <a style="left:642px">About</a>
  <a style="left:734px">Shop</a>
  <a style="left:816px">Videos</a>
  <a style="left:913px">Lost Certificate</a>
  <a class="login" style="left:1100px">Log In</a>
</header>
<div class="brand"><span class="brand-dot"></span>BRIGHT HARBOR</div>

<section class="hero" role="img" aria-label="Film still: close-up of a fired cartridge casing in flight with the company name across it">
  <div class="play-film">
    <svg width="12" height="13" viewBox="0 0 12 13"><path d="M1 1 L11 6.5 L1 12 Z" fill="#fff"/></svg>
    PLAY FILM
  </div>
  <h1>Don't Settle For A<br>Gun Shop Class!</h1>
  <div class="btn btn-solid">Join Falconry Institute</div>
  <div class="btn btn-ghost">Get Tickets Now</div>
</section>

<section class="instructor">
  <svg class="abs" style="left:0;top:0" width="640" height="500">
    <circle cx="284" cy="235" r="174" fill="#e4181b"/>
    <circle cx="407" cy="272" r="184" fill="#8d8d8d" role="img" aria-label="Black and white portrait of instructor Brendan Osterlow in a suit"/>
  </svg>
  <div class="eyebrow abs" style="left:670px;top:112px">About the Instructor</div>
  <h2>BRENDAN OSTERLOW</h2>
  <p>Brendan Osterlow is a true security expert with 25 years of experience in the security industry. He has appeared on Ridgeline, KVN, TBR &amp; Summit news outlets. He has been Featured in numerous publications and has trained thousands to protect themselves and their homes from thugs and thieves. He is certified by both the NMTA &amp; the NWDFA as a firearms instructor. He is also an NMTA Range Safety Officer and Defensive Pistol Instructor.</p>
  <div class="seen-on">
    <div class="eyebrow">As Seen On</div>
    <div class="rule" style="width:36px;margin:11px auto 0"></div>
  </div>
</section>

<div class="media-badge" style="left:262px">Ridgeline<br>News</div>
<div class="media-badge" style="left:448px">Summit<br>News</div>
<div class="media-badge" style="left:632px;background:#ececec">KVN</div>
<div class="media-badge" style="left:816px">TBR</div>

<h2 class="training-title"><span class="hl">7 Levels</span> Training<br>Taking You<br><span class="hl">From Zero to Hero</span></h2>
<div class="rule abs" style="left:103px;top:1611px;width:58px"></div>
<p class="training-copy">Why do most people settle for a cheap &amp; quick concealed carry class? It's a fair question! Could you imagine a military soldier trained by a 2-hour class? How effective would they be in the heat of battle? If you want to be ready to SURVIVE an attack, YOU NEED MORE than a basic, run of the mill class! That's why we created a PROPRIETARY 7 LEVEL TRAINING SYSTEM to take you all the way to the peak of readiness!</p>

<svg class="abs" style="left:530px;top:1752px" width="28" height="46"><path d="M22 3 L6 23 L22 43" fill="none" stroke="#1a1a1a" stroke-width="3.5"/></svg>
<div class="level-card" style="left:601px;width:367px">
  <div class="photo" role="img" aria-label="Black and white photo of a semi-automatic pistol on a table" style="background:linear-gradient(135deg,#cfcfcf,#555 55%,#2a2a2a)"></div>
  <div class="label">LEVEL1&nbsp;&nbsp;&nbsp;CONCEALED CARRY CLASS</div>
</div>
<div class="level-card" style="left:1022px;width:178px">
  <div class="photo" role="img" aria-label="Photo of a student in ear protection aiming a pistol" style="background:linear-gradient(90deg,#dcdcdc,#8a8a8a 60%,#6a3a3a)"></div>
  <div class="label">LEVEL2&nbsp;&nbsp;&nbsp;DYNAMIC</div>
</div>
<svg class="abs" style="left:1130px;top:1760px" width="26" height="34"><path d="M6 3 L20 17 L6 31" fill="none" stroke="#fff" stroke-width="3"/></svg>
<div class="dots"><span class="on"></span><span></span><span></span><span></span><span></span><span></span><span></span></div>

<div class="section-head" style="top:2087px;font-size:26px;letter-spacing:4.5px">Watch Video to Know More</div>
<div class="rule abs" style="left:571px;top:2130px;width:58px"></div>

<div class="video-band"></div>
<div class="video-frame">
  <svg width="74" height="74" viewBox="0 0 74 74"><circle cx="37" cy="37" r="34" fill="none" stroke="#fff" stroke-width="3"/><path d="M29 23 L52 37 L29 51 Z" fill="#fff"/></svg>
</div>

<div class="stories-photo" role="img" aria-label="Darkened photo of a shooter wearing ear protection at the range"></div>
<div class="section-head" style="top:2705px;font-size:40px;letter-spacing:6px;color:var(--red)">Success Stories</div>
<div class="rule abs" style="left:571px;top:2770px;width:58px"></div>

<div class="story" style="left:103px;top:2852px">
  <div class="quote">“</div>
  <p>I had never held a gun when I took the Bright Harbor Guarding class and I'm hooked! I'm going all the way to level7! Thank you Bright Harbor Guarding!</p>
  <div class="who">Marisa K.</div>
  <div class="when">October 14,2017</div>
</div>
<div class="story" style="left:452px;top:2852px">
  <div class="quote">“</div>
  <p>I was mugged here in Jacksonville and lived in fear ever since. It stole my happiness and I became scared to go out. I'm a Level 4 student and I feel sorry for the next thug that tries me!</p>
  <div class="who" style="margin-top:14px">Delia R.</div>
  <div class="when">December 9,2017</div>
</div>
<div class="story" style="left:801px;top:2852px">
  <div class="quote">“</div>
  <p>I've been shooting for years and already had my concealed weapons license. My first class was a gun shop class and a waste of money. Brendan took the time to show me how to properly grip my gun and my shooting dramatically improved!</p>
  <div class="who">Owen P.</div>
  <div class="when">March 3,2018</div>
</div>

<section class="contact">
  <h2>BRENDAN OSTERLOW</h2>
  <div class="role">Nmta Firearms Instructor, Nwdfa Instructor &amp; Training Counsellor, News Correspondent, And Security Expert</div>
  <div class="details">
    <div>P.O. BOX 4182<br>HARBOR POINT, FL 32090</div>
    <div>BRIGHTHARBORGUARDING<br>@MAILBOX.COM</div>
    <div>LOCAL: 904-555-0142 (0142)<br>TOLL-FREE: 800-555-0199</div>
  </div>
  <div class="field-label" style="top:80px">Name*</div>
  <div class="field" style="top:100px;height:36px"></div>
  <div class="field-label" style="top:158px">Email*</div>
  <div class="field" style="top:177px;height:36px"></div>
  <div class="field-label" style="top:235px">Phone</div>
  <div class="field" style="top:254px;height:36px"></div>
  <div class="field-label" style="top:312px">Message</div>
  <div class="field" style="top:331px;height:121px"></div>
  <div class="send">SEND</div>
</section>

<footer class="site-footer">Copyright Bright Harbor Guarding 2021 - All Rights Reserved</footer>

</body>
</html>
```